QR TILL WORKS , CREDIT CARD PROCESSING EQUIPMENT

qrtillworks is a sub division of Tallow a credit car processing co.
dorian pell
14 cedar hollow ln
lindmoor pa 07312
suite 412

qrtillworks.example
cell 555-214-7730
office 555-861-2093
we sell pos systems to merchant who want to accept credit cards at there retail location.
black card would be nice buit open to different ideas

Target Market(s)

retail merchants

Industry/Entity Type

credit card processing

Contact Information for Business Card

card should include web site phone address

Colors

Designer to choose colors to be used in the design.

Requirements
Should not have
• red

```html
<!DOCTYPE html>
<html lang="en">
<head>
<meta charset="utf-8">
<title>QR Till Works — Business Card</title>
<link rel="stylesheet" href="https://fonts.googleapis.com/css2?family=Open+Sans:wght@400;600;700&display=swap">
<style>
  :root {
    --page: #ffffff;
    --card: #050505;
    --gold: #e8b713;
    --white: #ffffff;
  }
  * { margin: 0; padding: 0; box-sizing: border-box; }
  html, body {
    width: 1200px; height: 1200px; overflow: hidden;
    background: var(--page);
    font-family: "Open Sans", Arial, sans-serif;
  }
  .sheet { position: relative; width: 1200px; height: 1200px; }
  .card {
    position: absolute; left: 150px; width: 900px; height: 500px;
    background: var(--card); overflow: hidden;
  }
  .card--front { top: 70px; }
  .card--back { top: 630px; }

  .rule { position: absolute; height: 3px; background: var(--gold); top: 380px; }
  .rule--left { left: 0; width: 412px; }
  .rule--right { left: 768px; width: 132px; }
  .rule--full { left: 0; width: 900px; }

  .brand {
    position: absolute; display: flex; align-items: center; gap: 14px;
    color: var(--white); font-weight: 600; letter-spacing: 1px; white-space: nowrap;
  }
  .brand__dot { border-radius: 50%; background: var(--gold); flex: none; }
  .card--front .brand { left: 93px; top: 176px; font-size: 30px; }
  .card--front .brand__dot { width: 16px; height: 16px; }
  .card--back .brand { left: 50%; top: 210px; transform: translateX(-50%); font-size: 46px; }
  .card--back .brand__dot { width: 22px; height: 22px; }

  .holder {
    position: absolute; left: 437px; top: 142px;
    color: var(--white); font-size: 36px; letter-spacing: 0.5px; text-transform: uppercase;
    white-space: nowrap;
  }
  .holder__first { font-weight: 700; }
  .holder__last { font-weight: 400; }
  .holder__underline {
    position: absolute; left: 437px; top: 196px; width: 252px; height: 3px; background: var(--white);
  }
  .holder__underline::before {
    content: ""; position: absolute; left: 0; top: 0; width: 50px; height: 3px; background: var(--gold);
  }

  .contact { position: absolute; left: 430px; top: 270px; list-style: none; }
  .contact__item {
    display: flex; align-items: flex-start; gap: 14px;
    color: var(--gold); font-size: 21px; line-height: 28px; margin-bottom: 14px;
    white-space: nowrap;
  }
  .contact__item:first-child { margin-bottom: 8px; }
  .contact__icon { width: 28px; height: 28px; flex: none; }

  .site {
    position: absolute; left: 0; width: 100%; top: 425px; text-align: center;
    color: var(--white); font-size: 21px; letter-spacing: 0.5px;
  }
</style>
</head>
<body>
<main class="sheet">
  <section class="card card--front" aria-label="Card front">
    <div class="brand"><span class="brand__dot"></span>QR TILL WORKS</div>
    <h1 class="holder"><span class="holder__first">Dorian</span> <span class="holder__last">Pell</span></h1>
    <div class="holder__underline"></div>
    <div class="rule rule--left"></div>
    <div class="rule rule--right"></div>
    <ul class="contact">
      <li class="contact__item">
        <svg class="contact__icon" viewBox="0 0 28 28" fill="none" stroke="#fff" stroke-width="1.4">
          <circle cx="14" cy="14" r="12.5"/>
          <path d="M14 21s-5-5.2-5-8.6a5 5 0 0 1 10 0C19 15.8 14 21 14 21z"/>
          <circle cx="14" cy="12.4" r="1.8"/>
        </svg>
        <span>14 cedar hollow ln<br>lindmoor pa 07312 suite 412</span>
      </li>
      <li class="contact__item">
        <svg class="contact__icon" viewBox="0 0 28 28" fill="none" stroke="#fff" stroke-width="1.4">
          <circle cx="14" cy="14" r="12.5"/>
          <circle cx="14" cy="14" r="7"/>
          <ellipse cx="14" cy="14" rx="3" ry="7"/>
          <path d="M7 14h14M8 10.5h12M8 17.5h12"/>
        </svg>
        <span>qrtillworks.example</span>
      </li>
      <li class="contact__item">
        <svg class="contact__icon" viewBox="0 0 28 28" fill="none" stroke="#fff" stroke-width="1.4">
          <circle cx="14" cy="14" r="12.5"/>
          <path d="M9.5 8.5l2.5-.5 1.3 3-1.6 1.2a8 8 0 0 0 4 4l1.2-1.6 3 1.3-.5 2.5c-5 .8-10.7-4.9-9.9-9.9z"/>
        </svg>
        <span>555-214-7730</span>
      </li>
      <li class="contact__item">
        <svg class="contact__icon" viewBox="0 0 28 28" fill="none" stroke="#fff" stroke-width="1.4">
          <circle cx="14" cy="14" r="12.5"/>
          <path d="M8 20V9h7v11M15 12h5v8M7 20h14M10 11.5h1M12.5 11.5h1M10 14.5h1M12.5 14.5h1M10 17.5h1M12.5 17.5h1"/>
        </svg>
        <span>555-861-2093</span>
      </li>
    </ul>
  </section>

  <section class="card card--back" aria-label="Card back">
    <div class="brand"><span class="brand__dot"></span>QR TILL WORKS</div>
    <div class="rule rule--full"></div>
    <p class="site">qrtillworks.example</p>
  </section>
</main>
</body>
</html>
```